Family Nature Adventure Stay - Thistlebrook Hollow

Thistlebrook Hollow is a low environmental impact children’s farm stay and nature education experience in Devon England which presents families with the opportunity to get closer to nature.

While staying at Thistlebrook Hollow, guests will be encouraged to take part in organised nature and adventure based activities such as bird and butterfly spotting, making camps, mini beast hunts, egg collecting, star gazing, pond dipping and moth nights.

Think of the stuff you wanted to do with your parents when you were nine – fishing with Dad? Making a camp with your new friends? Clay face modelling with Mum? Convey this in your site design.

We need six pages designing:

1. Home Page
2. Accommodation & Booking
3. Events & Activities
4. Location & Interactive Map
5. Meet the Residents
6. Green Credentials

Sites we like:
http://www.craftlanehub.example/
I love this site
Full screen image slider
Stylish navigation
Very simple

www.morwennacycleworks.example
Simple design
Full screen slider
Lots of graphics
The feelof summer in the image
Moving navigation bar

http://www.glintware.example/
A really cool front page
If the images shown was a slider even better.
(I'm not hot on the length of the page)

http://platterhaus.example/
Really simple design
Very stylish
Slider half page
Great Nav icons
font for contact us

www.ninefoldstudio.example
very stylish
images
the idea of the photo book
Beautiful fonts

Target Market(s)

Our target market is young families with one or more children between 6 and 14 who love the great outddors

Industry/Entity Type

Education

Requirements
Must have
• General Design
The site in general should be very nature, holiday and children based. The natural environment, quality, adventure and comfort should be at the heart of the site.
A common styling should be used for all pages.
All pages should feature our telephone number.

The styling does not have to use elements from our logo.
Each page should have a common site navigation bar.

1. Home Page
The home page should include a brief description of what we are and what we offer. A simple page is required with a large image slider and may be a couple of other images.

The home page should feature links to our social media sites (Chatterbook & Tweetline) and the following: Heritage Keepers Guild, Timberland Stewardship Board, Garnet Vale, Nearby Beaches, Verdant Enterprise Honours.

Annexe sleeps 2+2 bed
Stables sleeps 4
Cosyburrow (Yurt) sleeps 4
Mossnest (Yurt) sleeps 4

Section should include a section for each accommodation include 360° view image, images, descriptions and embedded booking calendar from (stayplanner.example) that will feature rates and availability.
The section should note that the yurts have private bathrooms with hot showers and flushing toilets.
This section should link to the correct flyout in the interactive map to show the accommodation location.

3. Location & Interactive Map
The location map should show be a zoomable map showing our location in Devon (perhaps an embedded Mapwise map).

The map should show the layout of Thistlebrook hollow and the surrounding area with flyout images on mouse-over of certain areas with textbox descriptions. This includes the location of the accommodation, amenities, animal fields, and special sites of interest. (see SitePlan.gif for our basic map).

4. Activities & Events
This page details what we are about and what is available to see and do on site, next door at the Timberland Stewardship Board and Heritage Keepers Guild sites and nearby in Devon & Cornwall.

Activities include:
Bird and butterfly spotting, making camps, mini beast hunts, hen’s egg collecting, star gazing, pond dipping, moth nights, clay modelling, slingshot range, tree climbing, candle dipping, animal husbandry, dressing up box, story-telling, cycling, trekking, make a bird-box etc.

We intend to have competitions where children can win prizes (Thistlebrook Club)
Calendar of upcoming events
Thistlebrook club and free giveaway bath duck.
Sponsor the animals.

5. Meet the residents
This page should have a cool design like a card clash page that lists the residents and their main skills and abilities. This could be a slider, gallery based or other cool interactive feature.

The family: Colin, Rosalind and our daughters Wendy & Josephine

The animals:
Cats – Misty & Daisy the farm cats
Dogs – Pip & Fudge
Goats – Annie, Alice, Annabelle & Agatha
Sheep – Sean, Flossy & Dipstick
Chickens – Including Ronnie, Muddy, Fantastic Feathers, Lenhen & Penny
Rabbit & Guinea Pig – Angus and Funky

The wildlife:
Foxes
Badgers
Deer
Jays
Jackdaws
Sparrows
Frogs
Newts
Water boatmen
The trout
Dippers
Nuthatch
Thrush
Blackbird
Moths & Butterflies

6. Green Credentials
We have tried hard to incorporate green technologies and practices into our site. This page should showcase some of the features we have used.
Central log biomass hot water boiler (hot water and heating)
Short Rotation Coppice biomass willow plantation to supply our own logs
Rainwater runoff harvesting
Solar lighting
Water usage reduction
All electricity used is from 100% renewable sources
Off grid composting toilets
Recycled brick and concrete in the car parks
Willow Spiling (River bank protection)
Woodland management and replanting
Waste reduction & recycling point
Habitat improvement programme

The designer must be able to supply all images and graphics as part of the award. Only your own work will be accepted. Not images and designs by others.
Nice to have
• Colour schemes
Eggshell blue (9ADCED), Dark Blue (1F6991) and white
(Taken from our logo)

Green & Gold
(Fern Guards in the film Vast)

```html
<!DOCTYPE html>
<html lang="en">
<head>
<meta charset="utf-8">
<title>Thistlebrook Hollow – Annexe Sleeps</title>
<link href="https://fonts.googleapis.com/css2?family=Barlow+Semi+Condensed:wght@400;500;600&family=Arimo:wght@400;700&display=swap" rel="stylesheet">
<style>
:root{
  --eggshell:#9adced;
  --navy:#1f6991;
  --navy-deep:#1c5e86;
  --ink:#333;
  --muted:#777;
  --white:#fff;
  --grid:#e4e4e4;
  --avail:#0b8a1e;
  --sold:#e31b1b;
  --noinfo:#8b8b8b;
  --map-green:#2fae3a;
  --map-pale:#9fe38f;
}
*{box-sizing:border-box;margin:0;padding:0}
html,body{width:1134px;height:1200px;overflow:hidden;background:var(--white)}
body{position:relative;font-family:"Arimo",Arial,sans-serif;color:var(--ink)}
.abs{position:absolute}
.head-font{font-family:"Barlow Semi Condensed","Arial Narrow",sans-serif}

.topbar{left:0;top:0;width:1134px;height:38px;background:var(--navy)}
.phone{right:166px;top:2px;display:flex;align-items:center;gap:10px;color:var(--white);font-family:"Barlow Semi Condensed",serif;font-size:31px;letter-spacing:.5px}
.brand{left:170px;top:58px;display:flex;align-items:center;gap:14px}
.brand-dot{width:70px;height:70px;border-radius:50%;background:var(--eggshell)}
.brand-name{font-family:"Barlow Semi Condensed",sans-serif;font-weight:600;font-size:34px;color:var(--navy)}
.social-top{left:848px;top:80px;display:flex;gap:11px}
.social-top span{width:22px;height:22px;border-radius:50%;background:var(--navy)}

.nav{left:0;top:158px;width:1134px;height:36px;background:var(--eggshell)}
.nav ul{list-style:none;position:absolute;left:170px;top:0;display:flex;height:36px}
.nav li{font-family:"Barlow Semi Condensed",sans-serif;font-weight:500;font-size:17px;color:var(--navy);line-height:36px;padding:0 11px;text-transform:uppercase}
.nav li.active{background:var(--navy);color:var(--white);padding:0 14px}

.crumb{left:172px;top:210px;font-size:10.5px;color:#555}
.crumb b{font-weight:400;color:var(--navy)}
.h-title{font-family:"Barlow Semi Condensed",sans-serif;font-weight:600;font-size:22px;color:var(--navy);text-transform:uppercase}
.stars{left:484px;top:224px;display:flex;gap:1px}
.btn{height:27px;border:1px solid #c9c9c9;border-radius:4px;background:linear-gradient(#fafafa,#dedede);font-size:10.5px;font-weight:700;color:#444;display:flex;align-items:center;justify-content:center;box-shadow:0 1px 2px rgba(0,0,0,.25)}

.hero{left:172px;top:260px;width:549px;height:335px;background:linear-gradient(180deg,#b98a46 0%,#e0b467 35%,#c46a2e 70%,#8a4a22 100%);box-shadow:0 6px 8px -4px rgba(0,0,0,.4)}
.badge-360{left:652px;top:276px}
.thumbs{left:176px;top:514px;display:flex;gap:4px;padding:3px;background:var(--white)}
.thumbs div{width:103px;height:70px}

.site-map{left:731px;top:260px;width:240px;height:183px;background:linear-gradient(135deg,var(--map-green) 0%,var(--map-pale) 45%,#3aa0c8 75%,var(--map-green) 100%);border:2px solid #1c8b2a}
.info-box{left:731px;top:450px;width:240px;height:145px;border:2px solid #e2e2e2;background:var(--white)}
.info-box h3{font-family:"Barlow Semi Condensed",sans-serif;font-weight:500;font-size:21px;color:var(--navy);position:absolute;left:14px;top:9px}
.feat{position:absolute;left:14px;width:210px;display:flex;align-items:center;font-size:10.5px;font-weight:700;color:#555}
.feat i{width:14px;height:10px;background:#c8c8c8;border-radius:2px;margin-right:22px}
.feat svg{margin-left:auto}

.copy{left:176px;top:630px;width:412px;font-size:10.6px;line-height:19.2px;color:#666}
.copy p+p{margin-top:6px}

.label{font-size:9.5px;color:#333}
.field{height:17px;border:1px solid #9ab;background:var(--white);font-size:10.5px;display:flex;align-items:center;padding-left:3px}
.cal{width:108px;border:1px solid #c8c8c8;background:var(--white)}
.cal h4{background:var(--navy-deep);color:var(--white);font-size:9.5px;font-weight:400;text-align:center;height:15px;line-height:15px}
.cal table{border-collapse:separate;border-spacing:1px;width:100%}
.cal td{height:15px;font-size:9px;text-align:center;background:var(--grid);color:var(--white)}
.cal tr.dow td{background:#d6d6d6;color:#333}
.cal td.a{background:var(--avail)}
.cal td.s{background:var(--sold)}
.cal td.n{background:var(--noinfo)}
.legend{left:636px;top:862px;width:334px;display:flex;align-items:center;font-size:9px;color:#222}
.legend a{color:#5a2a85;text-decoration:underline}
.sw{width:13px;height:13px;display:inline-block;margin:0 3px 0 0}

.others{top:940px;width:136px;height:90px;box-shadow:0 4px 5px -2px rgba(0,0,0,.35)}
.room-a{background:linear-gradient(160deg,#6b5a44,#d9c7a4 50,#3b3b3d)}
.room-b{background:linear-gradient(160deg,#d9c7a4,#b28a55 60%,#4c4f57)}
.room-c{background:linear-gradient(160deg,#5f7b55,#c8c2b5 50%,#3b6f6a)}

.foot-top{left:0;top:1096px;width:1134px;height:36px;background:var(--navy)}
.foot-bottom{left:0;top:1132px;width:1134px;height:68px;background:var(--eggshell)}
.foot-links{left:165px;top:1107px;font-size:10.2px;color:var(--white);letter-spacing:.2px;word-spacing:1px}
.copyright{left:166px;top:1148px;font-size:11px;font-weight:700;color:#336}
.social-foot{left:615px;top:1143px;display:flex;gap:11px}
.social-foot span{width:27px;height:27px;border-radius:50%;background:var(--navy)}
.foot-brand{left:800px;top:1060px;display:flex;align-items:center;gap:10px}
.foot-brand .dot{width:48px;height:48px;border-radius:50%;background:var(--white)}
.foot-brand span{font-family:"Barlow Semi Condensed",sans-serif;font-weight:600;font-size:22px;color:var(--white)}
</style>
</head>
<body>

<div class="abs topbar"></div>
<div class="abs phone">
  <svg width="24" height="24" viewBox="0 0 24 24"><path fill="#fff" d="M6.6 10.8a15.1 15.1 0 0 0 6.6 6.6l2.2-2.2c.3-.3.7-.4 1-.2 1.1.4 2.3.6 3.6.6.6 0 1 .4 1 1V20c0 .6-.4 1-1 1A17 17 0 0 1 3 4c0-.6.4-1 1-1h3.5c.6 0 1 .4 1 1 0 1.3.2 2.5.6 3.6.1.3 0 .7-.2 1z"/></svg>
  01632 960482
</div>

<div class="abs brand"><div class="brand-dot"></div><div class="brand-name">Thistlebrook Hollow</div></div>
<div class="abs social-top"><span></span><span></span><span></span><span></span></div>

<nav class="abs nav">
  <ul>
    <li>Home</li>
    <li class="active">Accommodation &amp; Booking</li>
    <li>Location &amp; Interactive Map</li>
    <li>Activities &amp; Events</li>
    <li>Meet the Residents</li>
  </ul>
</nav>

<div class="abs crumb">Accomodation &amp; Booking &gt;&gt; <b>Annexe Sleeps</b></div>
<h1 class="abs h-title" style="left:172px;top:222px">Annexe Sleeps</h1>
<div class="abs stars">
  <svg width="88" height="17" viewBox="0 0 88 17">
    <defs><path id="star" d="M8 1l2.1 4.6 5 .5-3.8 3.3 1.1 4.9L8 11.8l-4.4 2.5 1.1-4.9L.9 6.1l5-.5z"/></defs>
    <use href="#star" x="0" fill="#3b9be0"/><use href="#star" x="17.5" fill="#3b9be0"/><use href="#star" x="35" fill="#3b9be0"/>
    <use href="#star" x="52.5" fill="#d0d0d0"/><use href="#star" x="70" fill="#d0d0d0"/>
  </svg>
</div>
<div class="abs btn" style="left:587px;top:217px;width:135px">Back to Accomodations</div>
<h2 class="abs h-title" style="left:732px;top:222px">Location Map</h2>

<div class="abs hero" role="img" aria-label="Interior of the annexe yurt with a bed under a netted canopy and timber lattice walls"></div>
<svg class="abs badge-360" width="58" height="58" viewBox="0 0 58 58">
  <circle cx="29" cy="29" r="26" fill="none" stroke="#fff" stroke-width="3"/>
  <rect x="17" y="15" width="24" height="16" rx="3" fill="#fff"/>
  <circle cx="29" cy="23" r="5" fill="#c58a45"/>
  <text x="29" y="45" font-family="Arial" font-weight="700" font-size="12" fill="#fff" text-anchor="middle">360°</text>
</svg>
<div class="abs thumbs">
  <div role="img" aria-label="Wooden yurt exterior on a lawn" style="background:linear-gradient(#9ab6c9,#7a5a3a 60%,#4f7a3a)"></div>
  <div role="img" aria-label="Garden pond with plants" style="background:linear-gradient(#3e6b2a,#6f9a4a 50%,#b0643a)"></div>
  <div role="img" aria-label="Yurt bedroom interior" style="background:linear-gradient(#e4d6bd,#b7834a 60%,#c24a3a)"></div>
  <div role="img" aria-label="Bright bathroom interior" style="background:linear-gradient(#9a9a9a,#dcdcdc)"></div>
  <div role="img" aria-label="River bank with trees" style="background:linear-gradient(#6b8f4a,#7c9c96 60%,#3e5c33)"></div>
</div>

<div class="abs site-map" role="img" aria-label="Site plan showing fields, ponds, the river and the yurt locations"></div>
<div class="abs info-box">
  <h3>Annexe sleeps</h3>
  <div class="feat" style="top:52px"><i></i>Fields<svg width="14" height="12" viewBox="0 0 14 12"><path d="M1 6l4 4 8-9" fill="none" stroke="#5cb82e" stroke-width="2.5"/></svg></div>
  <div class="feat" style="top:74px"><i></i>Ponds<svg width="14" height="12" viewBox="0 0 14 12"><path d="M1 6l4 4 8-9" fill="none" stroke="#bdbdbd" stroke-width="2.5"/></svg></div>
  <div class="feat" style="top:96px"><i></i>Yurts<svg width="14" height="12" viewBox="0 0 14 12"><path d="M1 6l4 4 8-9" fill="none" stroke="#bdbdbd" stroke-width="2.5"/></svg></div>
  <div class="feat" style="top:118px"><i></i>Mossnest (Yurt) sleeps 4<svg width="14" height="12" viewBox="0 0 14 12"><path d="M1 6l4 4 8-9" fill="none" stroke="#bdbdbd" stroke-width="2.5"/></svg></div>
</div>

<div class="abs copy">
  <p>Lorem ipsum dolor sit amet, consectetuer adipiscing elit, sed diam nonummy nibh euismod tincidunt ut laoreet dolore magna aliquam erat volutpat. Ut wisi enim ad minim veniam, quis nostrud exerci tation ullamcorper suscipit lobortis a facilisi.Lorem ipsum dolor sit amet, consectetuer adipiscing elit, sed diam nonummy nibh euismod tincidunt ut laoreet dolore magna aliquam erat volutpat. Ut wisi enim ad minim veniam, quis nostrud exerci tation ullamcorper suscipit lobortis a facilisi.</p>
  <p>Lorem ipsum dolor sit amet, consectetuer adipiscing elit, sed diam nonummy nibh euismod tincidunt ut laoreet dolore magnLorem ipsum dolor sit amet, consectetuer adipiscing elit, sed diam nonummy nibh euismod tincidunt ut laoreet dolore magna aliquam erat volutpat. Ut wisi enim ad minim veniam, quis nostrud exerci tation ullamcorper suscipit lobortis a facilisi.a aliquam erat volutpat. Ut wisi enim ad minim veniam, quis .</p>
</div>

<h2 class="abs h-title" style="left:635px;top:627px">Booking Calender</h2>
<div class="abs label" style="left:636px;top:667px">Product:</div>
<div class="abs label" style="left:746px;top:667px">From:</div>
<div class="abs label" style="left:825px;top:667px">To:</div>
<div class="abs field" style="left:636px;top:682px;width:103px">Standard double <svg style="margin-left:auto" width="13" height="15" viewBox="0 0 13 15"><rect width="13" height="15" fill="#c9dcf2"/><path d="M3 6l3.5 4L10 6z" fill="#234"/></svg></div>
<div class="abs field" style="left:746px;top:682px;width:62px">7/19/06</div>
<svg class="abs" style="left:810px;top:684px" width="13" height="13" viewBox="0 0 13 13"><rect x=".5" y="1.5" width="12" height="11" fill="#eee" stroke="#777"/><rect x=".5" y="1.5" width="12" height="3" fill="#999"/></svg>
<div class="abs field" style="left:825px;top:682px;width:60px">7/20/06</div>
<svg class="abs" style="left:887px;top:684px" width="13" height="13" viewBox="0 0 13 13"><rect x=".5" y="1.5" width="12" height="11" fill="#eee" stroke="#777"/><rect x=".5" y="1.5" width="12" height="3" fill="#999"/></svg>

<div class="abs cal" style="left:636px;top:720px">
  <h4>July 2006</h4>
  <table>
    <tr class="dow"><td>S</td><td>M</td><td>T</td><td>W</td><td>T</td><td>F</td><td>S</td></tr>
    <tr><td></td><td></td><td></td><td></td><td></td><td></td><td class="n">1</td></tr>
    <tr><td class="n">2</td><td class="n">3</td><td class="n">4</td><td class="n">5</td><td class="n">6</td><td class="n">7</td><td class="n">8</td></tr>
    <tr><td class="n">9</td><td class="n">10</td><td class="n">11</td><td class="n">12</td><td class="n">13</td><td class="n">14</td><td class="n">15</td></tr>
    <tr><td class="n">16</td><td class="n">17</td><td class="n">18</td><td class="s">19</td><td class="s">20</td><td class="s">21</td><td class="a">22</td></tr>
    <tr><td class="a">23</td><td class="a">24</td><td class="a">25</td><td class="s">26</td><td class="s">27</td><td class="s">28</td><td class="s">29</td></tr>
    <tr><td class="a">30</td><td class="a">31</td><td></td><td></td><td></td><td></td><td></td></tr>
  </table>
</div>
<div class="abs cal" style="left:749px;top:720px">
  <h4>August 2006</h4>
  <table>
    <tr class="dow"><td>S</td><td>M</td><td>T</td><td>W</td><td>T</td><td>F</td><td>S</td></tr>
    <tr><td></td><td></td><td class="s">1</td><td class="s">2</td><td class="s">3</td><td class="a">4</td><td class="a">5</td></tr>
    <tr><td class="a">6</td><td class="a">7</td><td class="s">8</td><td class="s">9</td><td class="a">10</td><td class="s">11</td><td class="a">12</td></tr>
    <tr><td class="a">13</td><td class="a">14</td><td class="a">15</td><td class="s">16</td><td class="s">17</td><td class="s">18</td><td class="a">19</td></tr>
    <tr><td class="a">20</td><td class="s">21</td><td class="s">22</td><td class="s">23</td><td class="s">24</td><td class="s">25</td><td class="a">26</td></tr>
    <tr><td class="s">27</td><td class="s">28</td><td class="s">29</td><td class="s">30</td><td class="a">31</td><td></td><td></td></tr>
    <tr><td></td><td></td><td></td><td></td><td></td><td></td><td></td></tr>
  </table>
</div>
<div class="abs cal" style="left:862px;top:720px">
  <h4>September 2006</h4>
  <table>
    <tr class="dow"><td>S</td><td>M</td><td>T</td><td>W</td><td>T</td><td>F</td><td>S</td></tr>
    <tr><td></td><td></td><td></td><td></td><td></td><td class="a">1</td><td class="a">2</td></tr>
    <tr><td class="a">3</td><td class="a">4</td><td class="a">5</td><td class="a">6</td><td class="a">7</td><td class="a">8</td><td class="a">9</td></tr>
    <tr><td class="a">10</td><td class="s">11</td><td class="s">12</td><td class="s">13</td><td class="s">14</td><td class="a">15</td><td class="a">16</td></tr>
    <tr><td class="a">17</td><td class="a">18</td><td class="a">19</td><td class="a">20</td><td class="a">21</td><td class="a">22</td><td class="a">23</td></tr>
    <tr><td class="a">24</td><td class="a">25</td><td class="a">26</td><td class="a">27</td><td class="a">28</td><td class="a">29</td><td class="a">30</td></tr>
    <tr><td></td><td></td><td></td><td></td><td></td><td></td><td></td></tr>
  </table>
</div>
<div class="abs legend">
  <a>Previous</a>
  <span style="margin-left:54px"><i class="sw" style="background:var(--avail)"></i>Available</span>
  <span style="margin-left:6px"><i class="sw" style="background:var(--sold)"></i>Sold Out</span>
  <span style="margin-left:6px"><i class="sw" style="background:var(--noinfo)"></i>No Information</span>
  <a style="margin-left:auto">Next</a>
</div>

<h2 class="abs h-title" style="left:176px;top:900px">Other Accommodation Availablity</h2>
<div class="abs btn" style="left:833px;top:900px;width:136px">View more accomodations</div>
<div class="abs others room-a" style="left:179px" role="img" aria-label="Dining room with wooden table and chairs"></div>
<div class="abs others room-b" style="left:342px" role="img" aria-label="Lounge with sofa and dining area"></div>
<div class="abs others room-c" style="left:505px" role="img" aria-label="Courtyard with plants and a blue door"></div>
<div class="abs others room-a" style="left:668px" role="img" aria-label="Dining room with wooden table and chairs"></div>
<div class="abs others room-b" style="left:833px" role="img" aria-label="Lounge with sofa and dining area"></div>

<div class="abs foot-top"></div>
<div class="abs foot-bottom"></div>
<div class="abs foot-links">HOME &nbsp;|&nbsp; ACCOMMODATION &amp; BOOKING &nbsp;|&nbsp; LOCATION &amp; INTERACTIVE MAP &nbsp;|&nbsp; ACTIVITIES &amp; EVENTS &nbsp;|&nbsp; MEET THE RESIDENTS</div>
<div class="abs copyright">Copyrights © 2013 Brightmoor Web. All rights reserved.</div>
<div class="abs social-foot"><span></span><span></span><span></span><span></span></div>
<div class="abs foot-brand"><div class="dot"></div><span>Thistlebrook Hollow</span></div>

</body>
</html>
```